Business Cards for a law firm

Business cards for our law firm. Use our silhoette logo and OAK HARBOR - check our website (www.oakharbor-legal.com)

Contact Information for Business Card

our silhouette logo, OAK HARBOR, 800-555-0147, Dorian Kestrup, dorian@oakharbor-legal.com

Requirements
Must have
• our silhouette logo, OAK HARBOR, 800-555-0147, Dorian Kestrup, dorian@oakharbor-legal.com

```html
<!DOCTYPE html>
<html lang="en">
<head>
<meta charset="utf-8">
<title>Oak Harbor – Business Cards</title>
<link rel="stylesheet" href="https://fonts.googleapis.com/css2?family=Cinzel:wght@600;700&family=Open+Sans:wght@400;600&display=swap">
<style>
  :root {
    --navy: #1b3370;
    --navy-soft: #2d4788;
    --white: #ffffff;
    --ink: #1f2a44;
    --backdrop: #e6e7ea;
    --figure-tint: #c9d1e3;
  }
  * { box-sizing: border-box; margin: 0; padding: 0; }
  html, body {
    width: 1200px; height: 840px; overflow: hidden;
    background: var(--backdrop);
  }
  .canvas { position: relative; width: 1200px; height: 840px; }

  .card {
    position: absolute;
    width: 620px; height: 354px;
    border-radius: 22px;
    overflow: hidden;
    box-shadow: 0 10px 28px rgba(0,0,0,.18);
  }
  .card--front { left: 60px; top: 60px; background: var(--navy); }
  .card--back { left: 520px; top: 426px; background: var(--white); }

  .figure-area {
    position: absolute;
    left: 30px; bottom: 0;
    width: 270px; height: 300px;
    border-radius: 10px 10px 0 0;
  }
  .card--front .figure-area { background: linear-gradient(180deg, var(--navy-soft), #3b5596); }
  .card--back .figure-area { background: linear-gradient(180deg, var(--figure-tint), #aebbd8); }

  .brand {
    position: absolute;
    font-family: "Cinzel", serif;
    font-weight: 700;
    letter-spacing: 2px;
    white-space: nowrap;
  }
  .card--front .brand {
    right: 40px; bottom: 40px;
    font-size: 32px; color: var(--white);
  }
  .card--back .brand {
    left: 330px; top: 44px;
    font-size: 28px; color: var(--navy);
  }

  .contact {
    position: absolute;
    left: 340px; top: 122px;
    font-family: "Open Sans", sans-serif;
    color: var(--ink);
  }
  .contact__name {
    font-family: "Cinzel", serif;
    font-weight: 700;
    font-size: 21px;
    color: var(--navy);
    letter-spacing: 1px;
    white-space: nowrap;
  }
  .contact__role { font-size: 15px; margin-bottom: 22px; }
  .contact__list { list-style: none; }
  .contact__item {
    display: flex; align-items: center; gap: 9px;
    font-size: 14.5px; line-height: 1; margin-bottom: 11px;
    white-space: nowrap;
  }
  .contact__icon { width: 16px; height: 16px; flex: none; fill: var(--navy); }
</style>
</head>
<body>
<main class="canvas">

  <section class="card card--front" aria-label="Business card front">
    <div class="figure-area" role="img" aria-label="Silhouette logo: two standing figures in white"></div>
    <p class="brand">OAK HARBOR</p>
  </section>

  <section class="card card--back" aria-label="Business card back">
    <div class="figure-area" role="img" aria-label="Silhouette logo: two standing figures in navy"></div>
    <p class="brand">OAK HARBOR</p>
    <div class="contact">
      <p class="contact__name">Dorian Kestrup</p>
      <p class="contact__role">Owner</p>
      <ul class="contact__list">
        <li class="contact__item">
          <svg class="contact__icon" viewBox="0 0 16 16" aria-hidden="true"><path d="M3.6 1.2l2.3 2.6-1.4 1.8c.9 2 2.5 3.6 4.5 4.5l1.8-1.4 2.6 2.3-1.4 2.4C6.9 14.6 1.4 9.1 1.2 3z"/></svg>
          800-555-0147
        </li>
        <li class="contact__item">
          <svg class="contact__icon" viewBox="0 0 16 16" aria-hidden="true"><path d="M1 3h14v10H1z M2 4l6 5 6-5" fill="none" stroke="#1b3370" stroke-width="1.6"/></svg>
          dorian@oakharbor-legal.com
        </li>
        <li class="contact__item">
          <svg class="contact__icon" viewBox="0 0 16 16" aria-hidden="true"><circle cx="8" cy="8" r="7" fill="none" stroke="#1b3370" stroke-width="1.6"/><path d="M1 8h14M8 1c-3 3-3 11 0 14M8 1c3 3 3 11 0 14" fill="none" stroke="#1b3370" stroke-width="1.2"/></svg>
          www.oakharbor-legal.com
        </li>
      </ul>
    </div>
  </section>

</main>
</body>
</html>
```